National Intensive Course Provider needs an advert designed to appear in trams

We need an advertisement designed to put in trams, the dimensions are 660mm wide and 203mm height. We offer intensive driving courses all over the UK, allowing pupils to complete a full driving course within a week/two weeks with both the theory and practical tests included in the course (as required). We would like the colours used to be green and dark blue, maybe red also, whatever looks best from them colours really.

Key Points to highlight:
- Pass your driving test within 1 week
- Start your course as early as next week
- Both tests included as part of your course (if required)

I have attached some images which could be included in the design

```html
<!DOCTYPE html>
<html lang="en">
<head>
<meta charset="utf-8">
<title>Swiftpass Intensive Driving Courses – Tram Advert</title>
<link href="https://fonts.googleapis.com/css2?family=Roboto+Condensed:wght@700&family=PT+Sans+Narrow:wght@700&display=swap" rel="stylesheet">
<style>
  :root {
    --page: #ffffff;
    --navy: #0b0b47;
    --blue: #1b3c9e;
    --blue-light: #2f5cc4;
    --red: #e3000f;
    --silver: #d9d9dc;
    --white: #ffffff;
    --lime: #dfe82c;
    --logo-bg: #0a0c3c;
  }
  * { margin: 0; padding: 0; box-sizing: border-box; }
  html, body {
    width: 1200px;
    height: 391px;
    overflow: hidden;
    background: var(--page);
  }
  .advert {
    position: absolute;
    left: 18px;
    top: 18px;
    width: 1164px;
    height: 356px;
    overflow: hidden;
    background: var(--navy);
  }
  .advert__backdrop {
    position: absolute;
    inset: 0;
    width: 100%;
    height: 100%;
  }
  .brand {
    position: absolute;
    left: 56px;
    top: 62px;
    width: 262px;
    height: 180px;
    border: 2px solid var(--red);
    border-radius: 34px;
    background: var(--logo-bg);
    display: flex;
    flex-direction: column;
    align-items: center;
    justify-content: center;
    gap: 8px;
    color: var(--white);
    font-family: "Roboto Condensed", sans-serif;
    font-weight: 700;
    text-align: center;
  }
  .brand__name {
    font-size: 44px;
    letter-spacing: 1px;
    text-transform: uppercase;
    line-height: 1;
  }
  .brand__tagline {
    font-size: 18px;
    letter-spacing: 2px;
    text-transform: uppercase;
    line-height: 1.2;
  }
  .phone {
    position: absolute;
    left: 34px;
    top: 272px;
    color: var(--white);
    font-family: "Roboto Condensed", sans-serif;
    font-weight: 700;
    font-size: 62px;
    line-height: 1;
    letter-spacing: 1px;
  }
  .headline {
    position: absolute;
    right: 36px;
    top: 20px;
    color: var(--white);
    font-family: "Roboto Condensed", sans-serif;
    font-weight: 700;
    font-size: 80px;
    line-height: 76px;
    text-align: right;
    letter-spacing: -0.5px;
  }
  .start-badge {
    position: absolute;
    left: 410px;
    top: 156px;
    width: 200px;
    height: 200px;
    border-radius: 50%;
    background: radial-gradient(circle, #f4f4f4 60%, #bdbdc2 100%);
    display: flex;
    align-items: center;
    justify-content: center;
  }
  .start-badge__inner {
    width: 172px;
    height: 172px;
    border-radius: 50%;
    background: var(--red);
    display: flex;
    align-items: center;
    justify-content: center;
    color: var(--white);
    font-family: "PT Sans Narrow", sans-serif;
    font-weight: 700;
    font-size: 27px;
    line-height: 31px;
    text-align: center;
  }
  .pupil-photo {
    position: absolute;
    left: 636px;
    top: 186px;
    width: 216px;
    height: 216px;
    border-radius: 50%;
    background: radial-gradient(circle, #f2f2f2 60%, #a9a9b0 100%);
    display: flex;
    align-items: center;
    justify-content: center;
  }
  .pupil-photo__image {
    width: 196px;
    height: 196px;
    border-radius: 50%;
    background: linear-gradient(180deg, #4f7a3a 0%, #6f9a52 38%, #c9c9c9 55%, #b3151f 75%, #7d0d14 100%);
  }
  .included {
    position: absolute;
    right: 34px;
    top: 232px;
    color: var(--lime);
    font-family: "PT Sans Narrow", sans-serif;
    font-weight: 700;
    font-size: 28px;
    line-height: 36px;
    text-align: right;
  }
  .included__note { font-size: 24px; }
</style>
</head>
<body>
  <main class="advert">
    <svg class="advert__backdrop" viewBox="22 22 1456 446" preserveAspectRatio="none" aria-hidden="true">
      <defs>
        <linearGradient id="blueSweep" x1="0" y1="0" x2="1" y2="0">
          <stop offset="0" stop-color="#1b3c9e"/>
          <stop offset="0.6" stop-color="#2a52b8"/>
          <stop offset="1" stop-color="#1d3f9f"/>
        </linearGradient>
      </defs>
      <rect x="22" y="22" width="1456" height="446" fill="var(--navy)"/>
      <path d="M22,22 H680 C520,90 470,250 600,380 C660,430 740,458 850,468 H22 Z" fill="var(--red)"/>
      <path d="M22,22 H640 C490,90 440,250 575,382 C640,432 720,458 815,468 H22 Z" fill="var(--silver)"/>
      <path d="M22,22 H595 C455,90 410,250 545,384 C610,432 690,458 780,468 H22 Z" fill="url(#blueSweep)"/>
    </svg>

    <div class="brand">
      <span class="brand__name">Swiftpass</span>
      <span class="brand__tagline">Intensive Driving<br>Courses</span>
    </div>

    <p class="phone">000 000 0000</p>

    <h1 class="headline">Pass Your Driving<br>Test Within 1 Week</h1>

    <div class="start-badge">
      <p class="start-badge__inner">Start your<br>course as<br>early as next<br>week</p>
    </div>

    <div class="pupil-photo">
      <div class="pupil-photo__image" role="img" aria-label="Photo of a happy pupil holding a driving test pass certificate beside a red tuition car"></div>
    </div>

    <p class="included">Theory and practical<br>tests included as part of<br>your course <span class="included__note">(if required)</span></p>
  </main>
</body>
</html>
```